Building certification business in Sydney Australia

Brookvale Assessors is a small business that is currently growing and needs a profession looking website to attract customers and give them all the information they need. The main services we offer currently are pre-purchase building inspections for purchasers and other areas of construction consultancy including pool fencing certificates. Please see attached logos to incorporate to also match colour schemes with. Thanks!

Target Market(s)

Prospective buyers and home owners

Industry/Entity Type

Small Business

Requirements
Must have
• Promote the main services from the home page. Being able to select the type of service/certificate required from the main page and be directed to a specific page that deals with only that service containing the relevant information for that item.
Nice to have
• Small emphasis on the location of our office and areas we service etc.

```html
<!DOCTYPE html>
<html lang="en">
<head>
<meta charset="utf-8">
<title>Brookvale Assessors</title>
<link rel="stylesheet" href="https://fonts.googleapis.com/css2?family=PT+Sans:ital,wght@0,400;0,700;1,400&family=Archivo:wght@800&display=swap">
<style>
:root{
  --blue:#1a76bd;
  --navy:#1d2b3c;
  --text:#2a2a2a;
  --muted:#777;
  --light:#f6f6f6;
  --rule:#dfe3e7;
  --hero-a:#a9c7db;
  --hero-b:#6f9ec0;
}
*{margin:0;padding:0;box-sizing:border-box}
html,body{width:1200px;height:2161px;overflow:hidden}
body{position:relative;font-family:"PT Sans",sans-serif;color:var(--text);background:#fff}
.abs{position:absolute}
.topbar{left:0;top:0;width:1200px;height:55px;background:var(--light);font-size:13px;color:#333}
.topbar .contact{left:134px;top:19px;display:flex;gap:26px;align-items:center}
.topbar .contact span{display:flex;align-items:center;gap:6px}
.social-top{right:134px;top:18px;display:flex;gap:22px}
.dot{width:14px;height:14px;border-radius:50%;background:#3b5d87;display:block}
.header{left:0;top:55px;width:1200px;height:118px;background:#fff}
.brand{left:134px;top:80px;display:flex;align-items:center;gap:12px}
.brand .mark{width:44px;height:44px;border:4px solid var(--navy);border-radius:8px}
.brand .name{font-size:27px;font-weight:700;color:var(--navy);line-height:1.05}
.nav{left:452px;top:102px;display:flex;font-size:16px;font-weight:700;color:var(--navy)}
.nav a{color:inherit;text-decoration:none;position:absolute;white-space:nowrap}
.nav a.active{color:var(--blue)}
.search{left:1031px;top:95px;width:34px;height:35px;border:2px solid var(--navy);border-radius:5px;display:flex;align-items:center;justify-content:center}
.hero{left:0;top:173px;width:1200px;height:572px;background:linear-gradient(90deg,var(--hero-a),var(--hero-b))}
.hero-title{left:137px;top:284px;font-family:"Archivo",sans-serif;font-weight:800;font-size:37px;line-height:46px;color:var(--navy)}
.card{left:134px;top:501px;width:297px;height:346px;background:#fff;border:1px solid var(--blue);text-align:center}
.card .photo{width:100%;height:133px;background:linear-gradient(135deg,#8a7a5c,#c9a45a 50%,#6d6f78)}
.ico-circle{width:58px;height:58px;border-radius:50%;background:#fff;border:2px solid var(--blue);display:flex;align-items:center;justify-content:center}
.card .ico-circle{position:absolute;left:118px;top:104px}
.card p{font-size:12.5px;color:#444;margin-top:52px;line-height:18px;padding:0 18px}
.btn{display:inline-block;margin-top:16px;border:1px solid var(--blue);color:var(--blue);font-size:13.5px;padding:8px 12px}
.svc-title{font-size:17px;font-weight:700;color:var(--navy)}
.svc-sub{font-size:12.5px;color:#555;margin-top:2px}
.card .svc-title{margin-top:22px}
.mini{width:298px;text-align:center}
.mini .bar{position:absolute;top:0;left:0;width:100%;height:3px;background:#6b6b6b}
.mini .ico-circle{position:absolute;top:-29px;left:120px;border-color:#666}
.mini .txt{position:absolute;top:42px;width:100%}
.popular{left:0;top:905px;width:1200px;height:500px;background:var(--light)}
.sec-center{left:0;top:940px;width:1200px;text-align:center;font-size:25px;color:var(--navy)}
.sec-center b,.sec-left b{color:var(--blue);font-weight:700}
.rule{height:1px;background:var(--rule)}
.accent{height:3px;background:var(--blue)}
.item{display:flex;gap:17px;width:300px}
.item .box{width:58px;height:58px;border:1px solid var(--blue);border-radius:2px;flex:none;display:flex;align-items:center;justify-content:center;background:#fff}
.item .box.fill{background:var(--blue)}
.item h3{font-size:18px;font-weight:700;color:#333;margin-top:-3px}
.item p{font-size:12.5px;color:#888;line-height:17px;margin-top:3px}
.sec-left{font-size:25px;color:var(--navy)}
.tile{height:189px}
.tile.blue{background:var(--blue);color:#fff;padding:22px 19px}
.tile.blue h4{font-size:18px;font-weight:700;line-height:27px}
.tile.blue p{font-size:13px;line-height:18px;margin-top:6px}
.read{display:inline-block;background:#26384e;color:#fff;font-size:12px;padding:5px 8px;margin-top:12px}
.blogband{left:0;top:1760px;width:1200px;height:310px;background:var(--light)}
.quote{left:778px;top:1852px;width:288px;font-size:13px;font-style:italic;color:#666;line-height:22.5px}
.qmark{font-size:40px;color:#bbb;font-family:Georgia,serif;font-style:normal;line-height:0}
.footer-brand{left:958px;top:2085px;display:flex;align-items:center;gap:8px;font-size:17px;font-weight:700;color:var(--navy)}
.footer-brand i{width:26px;height:26px;border:3px solid var(--navy);border-radius:4px;display:block}
.copy{right:140px;top:2129px;font-size:11.5px;color:#666}
.social-foot{left:137px;top:2107px;display:flex;gap:18px;align-items:center}
.social-foot .dot{width:18px;height:18px;border-radius:3px;background:#4d5a6a}
.social-foot .dot.first{background:#fff;border:1px solid #3b5d87}
</style>
</head>
<body>

<div class="abs topbar">
  <div class="abs contact">
    <span><svg width="12" height="12" viewBox="0 0 24 24"><path d="M6 2l4 5-2 3c1 3 3 5 6 6l3-2 5 4-3 4C10 21 3 14 2 5z" fill="#3b5d87"/></svg>+61 2 5550 1234</span>
    <span><svg width="16" height="11" viewBox="0 0 16 11"><rect x=".5" y=".5" width="15" height="10" fill="none" stroke="#3b5d87"/><path d="M.5.5L8 6l7.5-5.5" fill="none" stroke="#3b5d87"/></svg>hello@brookvale-assessors.example</span>
  </div>
  <div class="abs social-top" aria-label="Social links">
    <i class="dot"></i><i class="dot"></i><i class="dot"></i><i class="dot"></i>
  </div>
</div>

<div class="abs header">
  <div class="abs brand" style="left:134px;top:22px">
    <i class="mark"></i>
    <div class="name">Brookvale<br>Assessors</div>
  </div>
  <nav class="abs nav" style="left:0;top:47px">
    <a class="active" style="left:452px">HOME</a>
    <a style="left:530px">ABOUT US</a>
    <a style="left:638px">SERVICE</a>
    <a style="left:732px">CERTIFICATION</a>
    <a style="left:876px">BLOG</a>
    <a style="left:948px">CONTACT</a>
  </nav>
  <div class="abs search" style="top:40px">
    <svg width="16" height="16" viewBox="0 0 16 16"><circle cx="6.5" cy="6.5" r="5" fill="none" stroke="#1d2b3c" stroke-width="2"/><path d="M10 10l4 4" stroke="#1d2b3c" stroke-width="2"/></svg>
  </div>
</div>

<div class="abs hero" role="img" aria-label="Smiling engineer in a hard hat holding rolled plans, in front of a line-drawn city skyline with cranes"></div>
<h1 class="abs hero-title">WELCOME TO<br>BROOKVALE ASSESSORS</h1>

<div class="abs card">
  <div class="photo" role="img" aria-label="Construction team reviewing plans on site"></div>
  <div class="ico-circle"><svg width="26" height="26" viewBox="0 0 26 26"><rect x="4" y="8" width="7" height="16" fill="#1a76bd"/><rect x="13" y="3" width="9" height="21" fill="#1a76bd"/><path d="M2 24h22" stroke="#1a76bd" stroke-width="2"/></svg></div>
  <p>Consectetur adipiscing elitivamus site blandit Euerat pulvinar convallisliquam imperdiet</p>
  <span class="btn">Show More Detlias</span>
  <div class="svc-title">Construction Consultancy</div>
  <div class="svc-sub">Neque eget scelerisque uere.</div>
</div>

<div class="abs mini" style="left:451px;top:745px">
  <div class="bar"></div>
  <div class="ico-circle"><svg width="22" height="24" viewBox="0 0 22 24"><rect x="4" y="2" width="14" height="21" fill="none" stroke="#666" stroke-width="2"/><path d="M8 7h2M12 7h2M8 11h2M12 11h2M8 15h2M12 15h2" stroke="#666" stroke-width="2"/></svg></div>
  <div class="txt"><div class="svc-title">Building Inspections</div><div class="svc-sub">Neque eget scelerisque uere.</div></div>
</div>
<div class="abs mini" style="left:768px;top:745px">
  <div class="bar"></div>
  <div class="ico-circle"><svg width="26" height="22" viewBox="0 0 26 22"><path d="M2 10q3-3 6 0t6 0 6 0 4 0M2 15q3-3 6 0t6 0 6 0 4 0M2 20q3-3 6 0t6 0 6 0 4 0" fill="none" stroke="#666" stroke-width="1.8"/><path d="M17 9V2h4" fill="none" stroke="#666" stroke-width="1.8"/></svg></div>
  <div class="txt"><div class="svc-title">Pool Fencing</div><div class="svc-sub">Neque eget scelerisque uere.</div></div>
</div>

<section class="abs popular"></section>
<h2 class="abs sec-center" style="font-weight:400">Our Most <b>Populer</b> Service</h2>
<div class="abs rule" style="left:133px;top:995px;width:933px"></div>
<div class="abs accent" style="left:533px;top:993px;width:137px"></div>

<div class="abs item" style="left:134px;top:1053px"><div class="box fill"><svg width="32" height="28" viewBox="0 0 32 28"><path d="M16 2v8M8 10h16l4 8H4z" fill="none" stroke="#fff" stroke-width="2"/><rect x="3" y="18" width="26" height="7" fill="#fff"/></svg></div><div><h3>Inspection &amp; Testing</h3><p>Lorem ipsum dolor sit amet, consect etur adipiscing elit.</p></div></div>
<div class="abs item" style="left:451px;top:1053px"><div class="box"><svg width="32" height="30" viewBox="0 0 32 30"><path d="M8 28V4h20M8 4l6 6M20 4v10" fill="none" stroke="#1a76bd" stroke-width="2.5"/><rect x="4" y="24" width="10" height="5" fill="#1a76bd"/><rect x="17" y="14" width="7" height="6" fill="#1a76bd"/></svg></div><div><h3>Vestibulum iaculis lacinia</h3><p>Lorem ipsum dolor sit amet, consect etur adipiscing elit.</p></div></div>
<div class="abs item" style="left:768px;top:1053px"><div class="box"><svg width="30" height="30" viewBox="0 0 30 30"><path d="M9 4v22M5 4h8M21 4v22M17 10h8" stroke="#1a76bd" stroke-width="3"/></svg></div><div><h3>Master Palning Work</h3><p>Lorem ipsum dolor sit amet, consect etur adipiscing elit.</p></div></div>

<div class="abs item" style="left:134px;top:1168px"><div class="box"><svg width="32" height="28" viewBox="0 0 32 28"><path d="M4 16l12 8 12-8-12-6z" fill="#1a76bd"/><path d="M8 4l10 8" stroke="#1a76bd" stroke-width="3"/></svg></div><div><h3>Vestibulum iaculis lacinia</h3><p>Lorem ipsum dolor sit amet, consect etur adipiscing elit.</p></div></div>
<div class="abs item" style="left:451px;top:1168px"><div class="box"><svg width="32" height="26" viewBox="0 0 32 26"><rect x="4" y="6" width="22" height="16" rx="3" fill="none" stroke="#1a76bd" stroke-width="2.5"/><circle cx="15" cy="14" r="4" fill="none" stroke="#1a76bd" stroke-width="2.5"/><path d="M26 18h4" stroke="#1a76bd" stroke-width="2.5"/></svg></div><div><h3>Pool fencing</h3><p>Lorem ipsum dolor sit amet, consect etur adipiscing elit.</p></div></div>
<div class="abs item" style="left:768px;top:1168px"><div class="box"><svg width="34" height="28" viewBox="0 0 34 28"><rect x="4" y="20" width="24" height="6" rx="3" fill="#1a76bd"/><rect x="8" y="12" width="10" height="8" fill="#1a76bd"/><path d="M18 14l8-8 4 6" fill="none" stroke="#1a76bd" stroke-width="2.5"/></svg></div><div><h3>New Technologies</h3><p>Lorem ipsum dolor sit amet, consect etur adipiscing elit.</p></div></div>

<div class="abs item" style="left:134px;top:1284px"><div class="box"><svg width="32" height="28" viewBox="0 0 32 28"><path d="M16 2v8M8 10h16l4 8H4z" fill="none" stroke="#1a76bd" stroke-width="2"/><rect x="3" y="18" width="26" height="7" fill="#1a76bd"/></svg></div><div><h3>Building Innovation</h3><p>Lorem ipsum dolor sit amet, consect etur adipiscing elit.</p></div></div>
<div class="abs item" style="left:451px;top:1284px"><div class="box"><svg width="30" height="30" viewBox="0 0 30 30"><path d="M7 12a8 8 0 0116 0z" fill="#1a76bd"/><rect x="10" y="13" width="10" height="6" fill="#1a76bd"/><path d="M5 29v-5q0-4 5-4h10q5 0 5 4v5z" fill="#1a76bd"/></svg></div><div><h3>Project Management</h3><p>Lorem ipsum dolor sit amet, consect etur adipiscing elit.</p></div></div>
<div class="abs item" style="left:768px;top:1284px"><div class="box"><svg width="32" height="26" viewBox="0 0 32 26"><path d="M2 2h28v22H2zM2 9h28M2 17h28M12 2v7M22 2v7M8 9v8M18 9v8M28 9v8M12 17v7M22 17v7" fill="none" stroke="#1a76bd" stroke-width="2"/></svg></div><div><h3>Moulded Bricks</h3><p>Lorem ipsum dolor sit amet, consect etur adipiscing elit.</p></div></div>

<h2 class="abs sec-left" style="left:133px;top:1440px;font-weight:400">Featured <b>Projects</b></h2>
<div class="abs rule" style="left:133px;top:1484px;width:933px"></div>
<div class="abs tile blue" style="left:134px;top:1518px;width:218px"><h4>CONSTRUCTION<br>CONSULTANCY</h4><p>Nullam pretium sodales sem, vel sollicitudin...</p><span class="read">Read More</span></div>
<div class="abs tile" style="left:372px;top:1518px;width:217px;background:linear-gradient(180deg,#9cc3e6,#2f4250)" role="img" aria-label="City skyline across a river"></div>
<div class="abs tile" style="left:609px;top:1518px;width:219px;background:linear-gradient(135deg,#c9b8a2,#7a7f86)" role="img" aria-label="Worker in a hard hat on a scaffold"></div>
<div class="abs tile" style="left:847px;top:1518px;width:219px;background:linear-gradient(180deg,#c6d7e4,#8e8c86)" role="img" aria-label="Construction site with cranes"></div>

<section class="abs blogband"></section>
<h2 class="abs sec-left" style="left:133px;top:1790px;font-weight:400">Latest from Blog</h2>
<div class="abs rule" style="left:133px;top:1835px;width:616px"></div>
<div class="abs accent" style="left:133px;top:1833px;width:62px"></div>
<div class="abs tile blue" style="left:134px;top:1855px;width:297px;height:152px"><h4>Buldiing Inspection</h4><p>Lorem ipsum dolor sit amet, consect etur adipiscing elit.</p><span class="read">Read More</span></div>
<div class="abs tile" style="left:451px;top:1855px;width:298px;height:152px;background:linear-gradient(180deg,#5f4c6b,#c8674a 55%,#2b2a3a)" role="img" aria-label="City skyline at sunset with a lit bridge"></div>
<svg class="abs" style="left:132px;top:2027px" width="82" height="14" viewBox="0 0 82 14"><circle cx="7" cy="7" r="6" fill="#1a76bd"/><circle cx="24" cy="7" r="5.5" fill="none" stroke="#1a76bd"/><circle cx="41" cy="7" r="5.5" fill="none" stroke="#1a76bd"/><circle cx="58" cy="7" r="5.5" fill="none" stroke="#1a76bd"/><circle cx="75" cy="7" r="5.5" fill="none" stroke="#1a76bd"/></svg>

<h2 class="abs sec-left" style="left:778px;top:1790px;font-weight:400">Testimonials</h2>
<div class="abs rule" style="left:778px;top:1835px;width:288px"></div>
<div class="abs accent" style="left:778px;top:1833px;width:62px"></div>
<div class="abs quote"><span class="qmark">&ldquo;</span> Lorem ipsum dolor sit amet, consectetur adipis ng eli Praesent interdum sodales nunc id finisit bus. Proin faucibus felis tellus, facilisis looreet lacus auctor inroin fauc ibus felis tellus, dolor facilisis looreet lacus auctor inmoprasentrbi sed mi id... <span class="qmark" style="float:right;margin-top:22px">&rdquo;</span></div>
<div class="abs" style="left:778px;top:1981px;width:58px;height:52px;background:linear-gradient(135deg,#8a8f96,#3c4046)" role="img" aria-label="Client portrait"></div>
<div class="abs" style="left:850px;top:1998px;font-size:13px;color:var(--blue)">— Lorem Ispumlar</div>

<div class="abs social-foot" aria-label="Social links"><i class="dot first"></i><i class="dot"></i><i class="dot"></i><i class="dot"></i><i class="dot"></i><i class="dot"></i></div>
<div class="abs footer-brand"><i></i>Brookvale Assessors</div>
<div class="abs copy">© 2014 BROOKVALE ASSESSORS.</div>

</body>
</html>
```